Business Card Design Project for Investment Fund

Orvanel Asset Partners is an emerging wealth management firm based in New Jersey. It offers superior investment returns to high net worth individuals and institutions by finding undervalued assets.
We recently selected a company logo which was inspired by the Tucana constellation. Beta Tucanae is a group of six stars, containing star cluster 47 Tucanae, rated the second brightest object in the sky.
Now we need a business card design. Since we are an investment firm, the design should project a sense of stability, growth and professionalism. The owner is interested in something simple yet striking, which of course is consistent with the logo.
Target Market(s)
Wealthy individuals, probably middle aged or older, in the US
Industry/Entity Type
Investment

```html
<!DOCTYPE html>
<html lang="en">
<head>
<meta charset="utf-8">
<title>Orvanel Asset Partners – Business Cards</title>
<link href="https://fonts.googleapis.com/css2?family=Open+Sans:wght@400;600;700&display=swap" rel="stylesheet">
<style>
  :root {
    --stage: #e8e5e0;
    --card-white: #ffffff;
    --navy: #14187a;
    --navy-deep: #0b0c63;
    --royal: #1f3fc4;
    --royal-bright: #2b55e0;
    --charcoal: #3b4048;
    --grey: #5b6068;
    --rule: #c9ccd2;
    --swoosh: #4a4e55;
    --white: #ffffff;
  }
  * { box-sizing: border-box; margin: 0; padding: 0; }
  html, body {
    width: 1200px; height: 466px; overflow: hidden;
    background: var(--stage);
    font-family: "Open Sans", Arial, sans-serif;
  }
  .stage { position: relative; width: 1200px; height: 466px; }

  .card {
    position: absolute; top: 84px; width: 525px; height: 299px;
    border-radius: 22px; overflow: hidden;
  }
  .card--front { left: 52px; background: var(--card-white); }
  .card--back {
    left: 625px;
    background: radial-gradient(ellipse 60% 75% at 50% 42%, var(--royal-bright) 0%, var(--royal) 30%, var(--navy) 70%, var(--navy-deep) 100%);
  }

  /* Front: brand block */
  .brand { position: absolute; text-align: center; }
  .card--front .brand { left: 12px; top: 50px; width: 230px; }
  .brand__mark {
    display: block; margin: 0 auto; width: 92px; height: 92px;
    border-radius: 14px; background: var(--royal);
  }
  .brand__name {
    font-weight: 600; color: var(--charcoal); line-height: 1.1;
  }
  .brand__name-main { display: block; font-size: 30px; letter-spacing: 3px; margin-top: 8px; }
  .brand__name-sub { display: block; font-size: 17px; margin-top: 4px; }

  .divider {
    position: absolute; left: 250px; top: 48px; width: 1px; height: 154px;
    background: var(--rule);
  }

  .person { position: absolute; left: 271px; top: 60px; }
  .person__name { font-size: 17px; font-weight: 700; color: var(--navy); }
  .person__title { font-size: 13px; color: var(--grey); letter-spacing: 0.6px; margin-top: 1px; }

  .contact { position: absolute; left: 271px; top: 122px; list-style: none; }
  .contact__item {
    display: flex; align-items: center; gap: 4px;
    font-size: 13px; color: var(--charcoal); height: 25px;
  }
  .contact__icon { width: 13px; height: 13px; flex: none; }

  .wave { position: absolute; left: 0; bottom: 0; width: 525px; height: 70px; }
  .address {
    position: absolute; left: 28px; bottom: 12px;
    font-size: 13px; color: var(--white);
  }

  /* Back */
  .card--back .brand { left: 0; top: 47px; width: 525px; }
  .card--back .brand__mark {
    width: 113px; height: 113px; border-radius: 16px;
    background: var(--royal-bright);
  }
  .card--back .brand__name { color: var(--white); }
  .card--back .brand__name-main { font-size: 34px; letter-spacing: 5px; margin-top: 12px; }
  .card--back .brand__name-sub { font-size: 20px; margin-top: 2px; }
  .back__web {
    position: absolute; left: 0; top: 245px; width: 525px; text-align: center;
    font-size: 14px; letter-spacing: 0.8px; color: var(--white);
  }
  .back__web strong { font-weight: 700; }
</style>
</head>
<body>
<main class="stage">

  <section class="card card--front" aria-label="Business card front">
    <div class="brand">
      <span class="brand__mark"></span>
      <p class="brand__name">
        <span class="brand__name-main">ORVANEL</span>
        <span class="brand__name-sub">Asset Partners</span>
      </p>
    </div>

    <div class="divider"></div>

    <div class="person">
      <p class="person__name">Dana Harlow</p>
      <p class="person__title">Marketing Manager</p>
    </div>

    <ul class="contact">
      <li class="contact__item">
        <svg class="contact__icon" viewBox="0 0 14 14"><circle cx="7" cy="7" r="6.3" fill="none" stroke="#1f3fc4" stroke-width="1.2"/><path d="M4.6 3.6c.5-.4 1-.3 1.2.2l.5 1.2c.1.3 0 .6-.3.8l-.4.3c.3.8.9 1.5 1.7 1.9l.4-.4c.2-.2.5-.3.8-.1l1.1.6c.4.2.5.8.1 1.2-.6.6-1.5.8-2.3.4C5.6 8.9 4.4 7.5 4 5.8c-.2-.8.1-1.6.6-2.2z" fill="#1f3fc4"/></svg>
        212-555-0148
      </li>
      <li class="contact__item">
        <svg class="contact__icon" viewBox="0 0 14 14"><rect x="1" y="3" width="12" height="8.5" rx="1.2" fill="#1f3fc4"/><path d="M1.5 3.8L7 8l5.5-4.2" fill="none" stroke="#fff" stroke-width="1"/></svg>
        dharlow@orvanelap.com
      </li>
      <li class="contact__item">
        <svg class="contact__icon" viewBox="0 0 14 14"><circle cx="7" cy="7" r="6" fill="#1f3fc4"/><g fill="none" stroke="#fff" stroke-width=".8"><ellipse cx="7" cy="7" rx="2.6" ry="6"/><path d="M1 7h12M2 4h10M2 10h10"/></g></svg>
        www.orvanelap.com
      </li>
    </ul>

    <svg class="wave" viewBox="0 0 525 70" preserveAspectRatio="none" aria-hidden="true">
      <defs>
        <linearGradient id="bandBlue" x1="0" y1="0" x2="1" y2="0">
          <stop offset="0" stop-color="#14187a"/>
          <stop offset="0.6" stop-color="#1f3fc4"/>
          <stop offset="1" stop-color="#14187a"/>
        </linearGradient>
      </defs>
      <path d="M0 30 C120 0 300 0 525 10 L525 70 L0 70 Z" fill="#4a4e55"/>
      <path d="M0 36 C130 8 310 8 525 20 L525 70 L0 70 Z" fill="#ffffff"/>
      <path d="M0 42 C140 14 320 16 525 26 L525 70 L0 70 Z" fill="#8a8f96"/>
      <path d="M0 46 C150 20 330 22 525 30 L525 70 L0 70 Z" fill="url(#bandBlue)"/>
    </svg>
    <p class="address">48 Harbor Ave., Newark, NJ 07102</p>
  </section>

  <section class="card card--back" aria-label="Business card back">
    <div class="brand">
      <span class="brand__mark"></span>
      <p class="brand__name">
        <span class="brand__name-main">ORVANEL</span>
        <span class="brand__name-sub">Asset Partners</span>
      </p>
    </div>
    <p class="back__web">www.<strong>orvanelap</strong>.com</p>
  </section>

</main>
</body>
</html>
```